Australian Trucking Company Requires Professional Looking Stationary

We require a professional looking stationary design that incorporates our newly designed logo.

Our business, called "Marlow Haul Contracting", provides contracting work, transport and logistics to business in Western Australia particularly with links to the mining sector.

We are a small business looking to expand and our new logo and our new stationary will help develop our brand image in our market place.

Target Market(s)

Businesses and Corporation with links to the Mining Sector

Industry/Entity Type

Small Business

Requirements
Must have
• The letterhead must have the following details:
The new logo

Text saying: "Marlow Holdings Pty Ltd (ACN 352 018 927) ATF The Marlow Discretionary Trust T/AS"
"ABN 72 483 910 615"
Address "P.O Box 817 Wexbridge WA, 6999"
Phone: 08 9555 0182
Email: marlowhaul@inboxmail.example

The text on the letterhead should be editable as the details are likely to change in the near future. Provision should be made for a website address all though one isn't available at the moment.

The styling, layout and font text is entirely up to the designer.

```html
<!DOCTYPE html>
<html lang="en">
<head>
<meta charset="utf-8">
<title>Marlow Haul Contracting – Stationery Set</title>
<link rel="stylesheet" href="https://fonts.googleapis.com/css2?family=Barlow+Condensed:wght@700&family=PT+Sans:ital,wght@1,400&family=Roboto:wght@400;700&display=swap">
<style>
  :root{
    --red:#c3161c;
    --red-deep:#7d0a10;
    --red-bright:#e3212a;
    --ink:#4a4a4a;
    --silver:#c9c9c9;
    --paper:#ffffff;
    --backdrop:#e8e5e1;
    --logo-font:"Barlow Condensed", sans-serif;
    --body-font:"Roboto", sans-serif;
  }
  *{margin:0;padding:0;box-sizing:border-box}
  html,body{width:1200px;height:515px;overflow:hidden}
  body{background:var(--backdrop);position:relative;font-family:var(--body-font);color:var(--ink)}
  .sheet{position:absolute;background:var(--paper);overflow:hidden;box-shadow:0 1px 4px rgba(0,0,0,.25)}
  .swoosh{position:absolute;left:0;bottom:0;width:100%}
  .brand{position:absolute;display:flex;align-items:flex-start;gap:5px}
  .brand-mark{width:30px;height:22px;background:#8c8c8c;flex:none}
  .brand-name{font-family:var(--logo-font);font-weight:700;color:var(--red);text-transform:uppercase;line-height:.9}
  .contact{position:absolute;font-size:5.5px;line-height:1.45}
  .contact li{list-style:none;display:flex;align-items:center;gap:4px}
  .contact .dot{width:3.5px;height:3.5px;border-radius:50%;background:var(--red);flex:none}
  .art{position:absolute}

  /* letterhead */
  .letterhead{left:62px;top:60px;width:269px;height:379px}
  .letterhead .brand{left:18px;top:10px}
  .letterhead .brand-name{font-size:12px}
  .letterhead .contact{right:14px;top:8px;text-align:right}
  .letterhead .contact li{justify-content:flex-end}
  .letterhead .abn{color:var(--red)}
  .letterhead .art{right:38px;top:222px;width:112px;height:124px;background:radial-gradient(ellipse at center,#e6e6e6,#f7f7f7 70%,#fff);opacity:.9}
  .letterhead .legal{position:absolute;right:8px;bottom:3px;font-size:4.6px;color:#fff}

  /* envelopes */
  .env-flap-red{left:385px;top:68px;width:307px;height:139px}
  .env-flap-red .art{left:138px;top:8px;width:42px;height:36px;background:linear-gradient(#b8141a,#8e0c12);opacity:.8}
  .env-flap-plain{left:478px;top:181px;width:307px;height:138px}
  .env-flap-plain .art{left:128px;top:10px;width:48px;height:38px;background:linear-gradient(#9a9a9a,#5f5f5f)}
  .env-front{left:385px;top:300px;width:307px;height:138px}
  .env-front .brand{left:8px;top:6px}
  .env-front .brand-name{font-size:11px}
  .env-front .address{position:absolute;left:8px;top:37px;font-size:5.3px;color:var(--red-deep)}
  .env-front .web{position:absolute;left:8px;bottom:6px;font-size:5.3px;color:var(--red-deep)}

  /* compliments slip */
  .compliments{left:833px;top:58px;width:299px;height:129px}
  .compliments .brand{left:12px;top:10px}
  .compliments .brand-name{font-size:11px}
  .compliments .title{position:absolute;right:10px;top:4px;font-family:"PT Sans",sans-serif;font-style:italic;font-size:15px;color:var(--red)}
  .compliments .contact{left:10px;top:84px;font-size:4.6px}
  .compliments .art{right:14px;bottom:6px;width:42px;height:44px;background:linear-gradient(#c94046,#a0141a);opacity:.7}

  /* business cards */
  .card-back{left:949px;top:221px;width:181px;height:103px;border-radius:6px;background:linear-gradient(90deg,var(--red-deep),var(--red) 55%,var(--red-bright))}
  .card-back .art{left:6px;top:2px;width:92px;height:100px;background:linear-gradient(135deg,#d9a0a3,#b3575c);opacity:.85}
  .card-back .web{position:absolute;left:90px;top:47px;font-size:7px;color:#fff;letter-spacing:.2px}
  .card-back .web b{font-weight:700}
  .card-front{left:833px;top:346px;width:181px;height:103px;border-radius:6px}
  .card-front .brand{left:7px;top:8px}
  .card-front .brand-name{font-size:11px}
  .card-front .holder{position:absolute;left:12px;top:60px;color:var(--red-deep)}
  .card-front .holder strong{display:block;font-size:7.5px;font-weight:700}
  .card-front .holder span{font-size:6px}
  .card-front .contact{right:6px;top:60px;text-align:right;color:#fff;font-size:5.2px}
  .card-front .contact li{justify-content:flex-end}
  .card-front .contact .dot{background:#fff}
</style>
</head>
<body>

<!-- Letterhead -->
<section class="sheet letterhead">
  <div class="brand"><span class="brand-mark"></span><span class="brand-name">Marlow Haul<br>Contracting</span></div>
  <ul class="contact">
    <li>08 9555 0182 <span class="dot"></span></li>
    <li>marlowhaul@inboxmail.example <span class="dot"></span></li>
    <li>www.marlowhaul.example <span class="dot"></span></li>
    <li>P.O Box 817 Wexbridge WA, 6999 <span class="dot"></span></li>
    <li class="abn">ABN 72 483 910 615</li>
  </ul>
  <div class="art" role="img" aria-label="Faint truck illustration watermark"></div>
  <svg class="swoosh" viewBox="0 0 269 44" preserveAspectRatio="none" height="44">
    <defs><linearGradient id="lhRed" x1="0" x2="1"><stop offset="0" stop-color="#7d0a10"/><stop offset=".5" stop-color="#c3161c"/><stop offset="1" stop-color="#8e0c12"/></linearGradient></defs>
    <path d="M0,30 C90,30 180,16 269,2 L269,44 L0,44Z" fill="url(#lhRed)"/>
    <path d="M0,27 C90,27 180,12 269,-1" fill="none" stroke="#bdbdbd" stroke-width="1.5"/>
    <path d="M0,31 C90,31 180,17 269,3" fill="none" stroke="#fff" stroke-width="1"/>
  </svg>
  <p class="legal">Marlow Holdings Pty Ltd (ACN 352 018 927) ATF The Marlow Discretionary Trust T/AS</p>
</section>

<!-- Envelope back, red flap -->
<section class="sheet env-flap-red">
  <svg class="flap" viewBox="0 0 307 60" width="307" height="60" style="position:absolute;left:0;top:0">
    <defs><linearGradient id="flapRed" x1="0" x2="1"><stop offset="0" stop-color="#9a0e14"/><stop offset=".5" stop-color="#e3212a"/><stop offset="1" stop-color="#9a0e14"/></linearGradient></defs>
    <path d="M0,0 H307 V8 C300,14 290,18 270,24 L175,50 C160,55 147,55 132,50 L37,24 C17,18 7,14 0,8Z" fill="url(#flapRed)"/>
  </svg>
  <div class="art" role="img" aria-label="Faint truck illustration on envelope flap"></div>
</section>

<!-- Envelope back, plain flap -->
<section class="sheet env-flap-plain">
  <svg viewBox="0 0 307 60" width="307" height="60" style="position:absolute;left:0;top:0">
    <path d="M2,2 C8,10 20,14 40,20 L140,50 C150,53 157,53 167,50 L267,20 C287,14 299,10 305,2" fill="none" stroke="#d4d4d4" stroke-width="1"/>
  </svg>
  <div class="art" role="img" aria-label="Grey truck illustration at flap point"></div>
</section>

<!-- Envelope front -->
<section class="sheet env-front">
  <div class="brand"><span class="brand-mark"></span><span class="brand-name">Marlow Haul<br>Contracting</span></div>
  <p class="address">P.O Box 817 Wexbridge WA, 6999</p>
  <p class="web">www.marlowhaul.example</p>
</section>

<!-- Compliments slip -->
<section class="sheet compliments">
  <div class="brand"><span class="brand-mark"></span><span class="brand-name">Marlow Haul<br>Contracting</span></div>
  <p class="title">With Compliments</p>
  <ul class="contact">
    <li><span class="dot"></span>08 9555 0182</li>
    <li><span class="dot"></span>marlowhaul@inboxmail.example</li>
    <li><span class="dot"></span>www.marlowhaul.example</li>
    <li><span class="dot"></span>P.O Box 817 Wexbridge WA, 6999</li>
  </ul>
  <svg class="swoosh" viewBox="0 0 299 60" preserveAspectRatio="none" height="60">
    <defs><linearGradient id="csRed" x1="0" x2="1"><stop offset="0" stop-color="#7d0a10"/><stop offset=".5" stop-color="#c3161c"/><stop offset="1" stop-color="#e3212a"/></linearGradient></defs>
    <path d="M0,56 C120,52 220,28 299,4 L299,60 L0,60Z" fill="url(#csRed)"/>
    <path d="M0,52 C120,48 220,24 299,0" fill="none" stroke="#bdbdbd" stroke-width="1.5"/>
    <path d="M0,57 C120,53 220,29 299,5" fill="none" stroke="#fff" stroke-width="1"/>
  </svg>
  <div class="art" role="img" aria-label="Faint truck illustration on red band"></div>
</section>

<!-- Business card, back -->
<section class="sheet card-back">
  <div class="art" role="img" aria-label="Large pale truck front illustration"></div>
  <p class="web">www.<b>marlowhaul</b>.example</p>
</section>

<!-- Business card, front -->
<section class="sheet card-front">
  <div class="brand"><span class="brand-mark"></span><span class="brand-name">Marlow Haul<br>Contracting</span></div>
  <svg class="swoosh" viewBox="0 0 181 62" preserveAspectRatio="none" height="62">
    <defs><linearGradient id="bcRed" x1="0" x2="1"><stop offset="0" stop-color="#7d0a10"/><stop offset=".5" stop-color="#c3161c"/><stop offset="1" stop-color="#e3212a"/></linearGradient></defs>
    <path d="M0,36 C60,34 120,18 181,2 L181,62 L0,62Z" fill="url(#bcRed)"/>
    <path d="M0,32 C60,30 120,14 181,-2" fill="none" stroke="#bdbdbd" stroke-width="1.5"/>
    <path d="M0,37 C60,35 120,19 181,3" fill="none" stroke="#fff" stroke-width="1"/>
  </svg>
  <div class="holder"><strong>Your Name</strong><span>Title</span></div>
  <ul class="contact">
    <li>08 9555 0182 <span class="dot"></span></li>
    <li>marlowhaul@inboxmail.example <span class="dot"></span></li>
    <li>www.marlowhaul.example <span class="dot"></span></li>
    <li>P.O Box 817 Wexbridge WA, 6999 <span class="dot"></span></li>
  </ul>
</section>

</body>
</html>
```